Creative, Modern and Conversion based Web Design

Kolvex Digital has recently launched a new logo and as part of our companies rebranding, we need a new website aimed towards the UK B2B marketplace.

The website needs to deliver a modern and creative website design whilst ensuring the design is tailored towards conversion optimisation.

This site must drive point of contact either from an online form, via a direct telephone call or Skype connection.

Our sales are all offline so the website will be a simple, elegant and stunning information portal.

Kolvex Digital offers Digital Marketing services to companies throughout the UK - our target audiences are companies that turnover a minimum of 3 million pounds a year and as such we need to deliver a professional image that installs confidence in our companies abilities.

We do not like websites that are reliant upon stock photography - we are happy for stock photography to be used in a small way however the site must not look like a template filled with stock photography.

What do we do

We supply digital marketing services to those companies who demand a strong return on investment - our company prides itself on delivering successful campaigns that help establish long-term profitable relationships.

A lot of the information presented on our old site is relevant today however the design sucks. So please use the information on our current website as a foundation for your design content.

I am looking for several page designs including

"Home Page" Desktop Version
"Service Page" Desktop Version
"Blog Page" Desktop Version

"Home Page" Mobile Version
"Service Page" Mobile Version
"Blog Page" Mobile Version

In the 1st instance please only submit a single design for the "Home Page" Desktop Version - those designers that we are impressed with will be asked to complete the other designs before a winner is selected.

I like modern clean fonts - the site needs to welcome the reader and encourage them to absorb the information - not to overload and make them leave.

The site must be designed to naturally fit our companies new logo.

NO TEMPLATES

Target Market(s)

B2b - 3 million turnover and above

Industry/Entity Type

Digital Marketing

Number of Pages Required

3 page

Requirements
Must have
• Blended well with the companies logo
• We need conversion optimisation to be a huge part of the design - we considered a conversation when a potential customer reaches out to use via - web form, telephone or skype
• The current content on the old website fits today's business but the design sucks.
• www.kolvexdigital-example.com
Nice to have
• We need 3 pages (in 2 variants Desktop and Mobile)
• Home Page
• Service Page
• Blog Page
• Please only deliver the "Home Page" desktop version - if we are happy with your design we will aks for the additional pages
Should not have
• No templates and not stock photo heavy design

```html
<!DOCTYPE html>
<html lang="en">
<head>
<meta charset="utf-8">
<title>Kolvex Digital – Search Marketing That Actually Delivers</title>
<link rel="stylesheet" href="https://fonts.googleapis.com/css2?family=Poppins:wght@300;400;500;600&display=swap">
<style>
:root{
  --blue:#1460ad;
  --blue-dark:#0d4f97;
  --blue-band:#0c5aa6;
  --blue-form:#1c6fc4;
  --sky:#abe0f1;
  --pale:#eaf5fb;
  --orange:#f47a20;
  --ink:#1f1f1f;
  --body:#555b62;
  --grey:#707478;
  --footer:#1b1b1b;
  --white:#fff;
}
*{box-sizing:border-box;margin:0;padding:0}
html,body{width:1200px;height:3180px;overflow:hidden;background:var(--white)}
body{font-family:"Poppins",sans-serif;color:var(--body);position:relative}
.abs{position:absolute}

/* header */
.site-header{position:absolute;left:0;top:0;width:1200px;height:95px}
.brand{left:86px;top:20px;display:flex;align-items:center;gap:10px}
.brand-mark{width:30px;height:30px;background:var(--grey)}
.brand-name{font-size:20px;font-weight:600;color:var(--grey);letter-spacing:.5px}
.contact-item{top:30px;display:flex;align-items:center;gap:12px;font-size:16px;color:var(--blue)}
.contact-item .dot{width:36px;height:36px;border-radius:50%;background:var(--grey);display:flex;align-items:center;justify-content:center}
.btn-contact{left:899px;top:29px;width:160px;height:40px;background:var(--blue-dark);color:var(--white);font-size:16px;display:flex;align-items:center;justify-content:center}
.menu-toggle{left:1092px;top:38px;width:20px}
.menu-toggle span{display:block;height:2px;background:var(--grey);margin-bottom:5px}

/* hero */
.hero{left:34px;top:95px;width:1132px;height:466px;background:var(--sky);text-align:center}
.hero h1{margin-top:35px;font-size:47px;font-weight:600;color:var(--blue);letter-spacing:.3px}
.hero p{font-size:21px;color:var(--ink);margin-top:2px}
.hero-art{position:absolute;left:273px;top:159px;width:603px;height:275px;border-radius:8px;background:radial-gradient(ellipse at 50% 50%,#d8f1f9 0%,#bfe7f4 60%,var(--sky) 100%)}

/* intro */
.intro{left:85px;top:645px;width:530px}
.intro h2{font-size:28px;font-weight:400;color:var(--blue);line-height:1.3}
.intro p{margin-top:20px;font-size:13.2px;line-height:28px;color:#4e4e4e}
.badges{left:85px;top:997px;display:flex;align-items:center;gap:30px}
.badge-partner{width:262px;height:92px;border:1px solid #ccc;background:var(--white);position:relative}
.badge-partner::before{content:"";position:absolute;left:0;top:0;width:12px;height:100%;background:#4a74c4}
.badge-partner::after{content:"";position:absolute;left:40px;top:22px;width:170px;height:46px;background:#dfe3e8;border-radius:4px}
.badge-small{display:flex;align-items:center;gap:8px}
.badge-small i{display:block;width:30px;height:30px;background:#f0a020;clip-path:polygon(0 100%,50% 0,100% 100%)}
.badge-small b{display:block;width:78px;height:26px;background:#e3e6ea;border-radius:3px}

/* form */
.consult{left:698px;top:628px;width:417px;height:487px;background:var(--blue-form);box-shadow:0 6px 18px rgba(0,0,0,.25)}
.consult-head{height:56px;background:var(--blue-dark);color:var(--white);font-size:20px;font-weight:500;display:flex;align-items:center;justify-content:center;letter-spacing:.4px}
.consult-intro{color:var(--white);text-align:center;font-size:15px;line-height:23px;margin:14px 30px 10px}
.field{margin:0 30px 9px 32px;height:36px;background:var(--white);font-size:12px;color:#999;padding:10px 10px}
.field.area{height:60px}
.privacy{margin:18px 32px 0;font-size:10.5px;line-height:14px;color:#d6e6f8}
.btn-send{margin:12px 30px 0 32px;height:36px;background:var(--orange);color:var(--white);font-size:16px;display:flex;align-items:center;justify-content:center}

/* tools band */
.tools{left:34px;top:1185px;width:1132px;height:222px;background:var(--pale);text-align:center}
.tools p{margin-top:38px;font-size:16px;font-weight:500;color:var(--ink)}
.tools p a{color:var(--blue);text-decoration:none;font-weight:400}
.tools-row{position:absolute;left:61px;top:85px;width:1008px;height:95px;background:var(--white);border:1px solid #d4dbe0;display:flex;align-items:center;justify-content:space-around;padding:0 30px}
.tool{height:30px;border-radius:4px}

/* services */
.services-title{left:0;top:1468px;width:1200px;text-align:center;font-size:32px;font-weight:600;color:var(--blue)}
.service{width:330px;text-align:center}
.service svg{display:block;margin:0 auto}
.service h3{margin-top:18px;font-size:15.5px;font-weight:400;color:var(--ink)}
.service p{margin-top:10px;font-size:13px;line-height:26px;color:#4e4e4e}
.read-more{display:inline-block;margin-top:12px;font-size:12.5px;color:#444;border-bottom:1px solid #888;line-height:16px}

/* stats */
.stats{left:34px;top:2180px;width:1132px;height:418px;background:var(--blue-band);overflow:hidden;text-align:center}
.stats h2{margin-top:60px;font-size:28px;font-weight:300;color:var(--white)}
.stats .waves{position:absolute;left:0;bottom:0}
.stat{position:absolute;top:120px;width:240px;text-align:center;color:var(--white)}
.stat .ring{width:178px;height:178px;margin:0 auto;border:7px solid var(--white);border-radius:50%;display:flex;align-items:center;justify-content:center;font-size:34px;font-weight:500;position:relative;z-index:1}
.stat span{display:block;margin-top:12px;font-size:18px;position:relative;z-index:1}
.stat-divider{position:absolute;top:130px;width:1px;height:150px;background:rgba(255,255,255,.25)}

/* diy seo */
.diy{left:0;top:2655px;width:1200px;text-align:center}
.diy h2{font-size:32px;font-weight:600;color:var(--blue)}
.diy h4{margin-top:2px;font-size:16px;font-weight:400;color:var(--ink)}
.diy p{width:990px;margin:18px auto 0;font-size:13px;line-height:28px;color:#4e4e4e}

/* footer */
.site-footer{left:34px;top:2926px;width:1132px;height:233px;background:var(--footer);color:#cfcfcf}
.foot-col{position:absolute;top:58px}
.foot-col h5{font-size:12px;font-weight:600;color:var(--white);letter-spacing:.6px;margin-bottom:18px}
.foot-col li{list-style:none;font-size:11.5px;line-height:20px}
.foot-col li::before{content:"›";margin-right:8px;color:#999}
.addr{font-size:11.5px;line-height:20px;padding-left:22px;position:relative}
.addr svg,.foot-line svg{position:absolute;left:0;top:2px}
.foot-line{position:relative;padding-left:26px;font-size:11.5px;line-height:20px;margin-bottom:12px}
</style>
</head>
<body>

<header class="site-header">
  <div class="abs brand"><div class="brand-mark"></div><div class="brand-name">Kolvex Digital</div></div>
  <div class="abs contact-item" style="left:438px">
    <div class="dot"><svg width="16" height="16" viewBox="0 0 24 24"><path fill="#fff" d="M6.6 10.8a15 15 0 0 0 6.6 6.6l2.2-2.2c.3-.3.7-.4 1-.2 1.1.4 2.3.6 3.6.6.6 0 1 .4 1 1V20c0 .6-.4 1-1 1A17 17 0 0 1 3 4c0-.6.4-1 1-1h3.5c.6 0 1 .4 1 1 0 1.3.2 2.5.6 3.6.1.3 0 .7-.2 1z"/></svg></div>
    +44 (0) 1632 960418
  </div>
  <div class="abs contact-item" style="left:677px">
    <div class="dot"></div>
    kolvexdigital_123
  </div>
  <a class="abs btn-contact">Contact Us</a>
  <div class="abs menu-toggle"><span></span><span></span><span></span></div>
</header>

<section class="abs hero">
  <h1>Search Marketing That Actualy Delivers</h1>
  <p>Search Marketing is our forte. Our client results highlight just how good we do it.</p>
  <div class="hero-art" role="img" aria-label="Illustration of a magnifying glass over a search bar, surrounded by charts, map pins and a laptop"></div>
</section>

<section class="abs intro">
  <h2>Do you want to see an enviable ROI on search marketing? It's possible – you've found us.</h2>
  <p>We know and understand the world of business. We know that ROI is the single most important metric in the marketing world. We've worked within some of the world's largest industries – such as finance, insurance, payday loans and health; where achieving above 100% ROI is often impossible. For us, it's just a challenge that can be overcome. Whether we're working with you to drive your Pay-Per-Click Marketing, Organic Search Marketing (SEO), Email Marketing or Lead Filtering &amp; Delivery – we always have your ROI in mind. That's why we're known as the ROI driven digital agency.</p>
</section>
<div class="abs badges">
  <div class="badge-partner"></div>
  <div class="badge-small"><i></i><b></b></div>
  <div class="badge-small"><i style="background:#f28c1e"></i><b></b></div>
</div>

<form class="abs consult">
  <div class="consult-head">GET YOUR 1-ON-1 CONSULTATION</div>
  <div class="consult-intro">Schedule a complimentary consultation with one of our in-house experts for FREE.</div>
  <div class="field">Name *</div>
  <div class="field">Email *</div>
  <div class="field">Phone *</div>
  <div class="field">Website *</div>
  <div class="field area">What are your SEO Challenges?</div>
  <div class="privacy">Kolvex Digital respects your privacy and will not misuse or sell your information.</div>
  <div class="btn-send">Send</div>
</form>

<section class="abs tools">
  <p>Handle your SEO in-house? Consider using our industry-leading <a>link outreach service</a> to bolster your efforts.</p>
  <div class="tools-row">
    <div class="tool" style="width:110px;background:#f7d7b8"></div>
    <div class="tool" style="width:100px;background:#f6c6bc"></div>
    <div class="tool" style="width:95px;background:#c3d9ef"></div>
    <div class="tool" style="width:95px;background:#dbe8c2"></div>
    <div class="tool" style="width:125px;background:#d6dfea"></div>
    <div class="tool" style="width:85px;background:#c6e6df"></div>
  </div>
</section>

<h2 class="abs services-title">Our Digital Marketing Services:</h2>

<div class="abs service" style="left:83px;top:1542px">
  <svg width="46" height="46" viewBox="0 0 46 46"><circle cx="20" cy="19" r="12" fill="none" stroke="#f07a22" stroke-width="5"/><path d="M28 28l11 11" stroke="#f07a22" stroke-width="6" stroke-linecap="round"/></svg>
  <h3>Organic Search</h3>
  <p>Attract traffic that converts and interacts with your brand through Organic. We implement both short-term and long-term campaigns to bolster your success.</p>
  <span class="read-more">READ MORE</span>
</div>
<div class="abs service" style="left:434px;top:1542px">
  <svg width="46" height="46" viewBox="0 0 46 46"><circle cx="21" cy="21" r="16" fill="none" stroke="#8cc63f" stroke-width="4"/><text x="21" y="28" text-anchor="middle" font-family="Poppins, sans-serif" font-size="18" font-weight="600" fill="#8cc63f">£</text><path d="M32 32l9 9" stroke="#8cc63f" stroke-width="4" stroke-linecap="round"/></svg>
  <h3>Paid Search</h3>
  <p>Drive highly converting traffic to your website. Our PPC campaigns are ROI-driven from the start – helping you to scale your business quickly.</p>
  <span class="read-more">READ MORE</span>
</div>
<div class="abs service" style="left:785px;top:1542px">
  <svg width="46" height="46" viewBox="0 0 46 46"><rect x="6" y="17" width="22" height="12" rx="6" transform="rotate(-45 17 23)" fill="none" stroke="#1a5fa8" stroke-width="4"/><rect x="18" y="17" width="22" height="12" rx="6" transform="rotate(-45 29 23)" fill="none" stroke="#1a5fa8" stroke-width="4"/></svg>
  <h3>Link Outreach</h3>
  <p>The core foundation of any search campaign. Our team of link outreachers are the best in the industry. We secure link placements that drive rankings.</p>
  <span class="read-more">READ MORE</span>
</div>

<div class="abs service" style="left:83px;top:1860px">
  <svg width="46" height="46" viewBox="0 0 46 46" stroke="#29b8d8" stroke-width="3"><path d="M23 23L8 8M23 23L38 8M23 23L8 38M23 23L38 38M23 23V4"/><g fill="#29b8d8" stroke="none"><circle cx="23" cy="23" r="6"/><circle cx="8" cy="8" r="4"/><circle cx="38" cy="8" r="4"/><circle cx="8" cy="38" r="4"/><circle cx="38" cy="38" r="4"/><circle cx="23" cy="4" r="3"/></g></svg>
  <h3>Social Media</h3>
  <p>Your followers are your most loyal customers. Let us develop a comprehensive strategy that aligns your brand with interests, while driving increased sales.</p>
  <span class="read-more">READ MORE</span>
</div>
<div class="abs service" style="left:434px;top:1860px">
  <svg width="46" height="46" viewBox="0 0 46 46"><circle cx="23" cy="9" r="5" fill="#e8413c"/><path d="M8 17h30l-11 13v12l-8-4v-8z" fill="#e8413c"/></svg>
  <h3>UX &amp; CRO</h3>
  <p>Let us dig into your analytic channels and identify where we can bolster your conversion rates while improving user experience.</p>
  <span class="read-more">READ MORE</span>
</div>
<div class="abs service" style="left:785px;top:1860px">
  <svg width="46" height="46" viewBox="0 0 46 46" fill="#3cb54a"><rect x="4" y="26" width="8" height="14"/><rect x="15" y="20" width="8" height="20"/><rect x="26" y="24" width="8" height="16"/><rect x="37" y="12" width="7" height="28"/><path d="M4 20L16 10l10 8 16-14" fill="none" stroke="#3cb54a" stroke-width="3"/></svg>
  <h3>Email Marketing</h3>
  <p>Our targeted email marketing campaigns allow you to segment users and deliver custom-tailored campaigns and promotions to different demographics.</p>
  <span class="read-more">READ MORE</span>
</div>

<section class="abs stats">
  <h2>We grow as our clients grow. That's what we love.</h2>
  <svg class="waves" width="1132" height="230" viewBox="0 0 1132 230" preserveAspectRatio="none">
    <path d="M0 120 C120 60 220 150 340 110 S560 40 700 100 S940 170 1132 70 V230 H0z" fill="#1668b5"/>
    <path d="M0 160 C150 110 260 190 420 150 S680 100 820 150 S1020 190 1132 130 V230 H0z" fill="#1f75c0"/>
  </svg>
  <div class="stat-divider" style="left:392px"></div>
  <div class="stat-divider" style="left:740px"></div>
  <div class="stat" style="left:94px"><div class="ring">117</div><span>Satisfied Clients</span></div>
  <div class="stat" style="left:445px"><div class="ring">215</div><span>Campaigns Finished</span></div>
  <div class="stat" style="left:796px"><div class="ring">1,798</div><span>Cups of Coffee</span></div>
</section>

<section class="abs diy">
  <h2>Handle SEO Yourself? Perfect.</h2>
  <h4>Hassle-Free Link Placements That Drive Rankings</h4>
  <p>Our link placements are used by some of the world's largest companies in the most difficult industries – such as payday loans, insurance, finance, health and legal. We use our link placement service in conjunction with our Organic Search (SEO) offerings; although some of our clients handle their SEO in-house and prefer to use our link placements to bolster their rankings.</p>
  <span class="read-more" style="margin-top:20px">READ MORE</span>
</section>

<footer class="abs site-footer">
  <div class="foot-col" style="left:78px">
    <h5>OUR KEY SERVICES</h5>
    <ul><li>Link Outreach</li><li>Organic Search (SEO)</li><li>Paid Search (PPC)</li><li>Social Media Marketing</li></ul>
  </div>
  <div class="foot-col" style="left:382px">
    <h5>OUR KEY SERVICES</h5>
    <ul><li>Link Outreach</li><li>Organic Search (SEO)</li><li>Paid Search (PPC)</li><li>Social Media Marketing</li></ul>
  </div>
  <div class="foot-col" style="left:686px">
    <h5>HARWICK OFFICE</h5>
    <div class="addr"><svg width="12" height="16" viewBox="0 0 12 16"><path d="M6 0a6 6 0 0 0-6 6c0 4.5 6 10 6 10s6-5.5 6-10a6 6 0 0 0-6-6zm0 8.5A2.5 2.5 0 1 1 6 3.5a2.5 2.5 0 0 1 0 5z" fill="#f47a20"/></svg>Kolvex Digital Ltd<br>The Granary<br>14 Orchard Row, Harwick<br>Harwick, HW4 2QT</div>
  </div>
  <div class="foot-col" style="left:907px;top:90px">
    <div class="foot-line"><svg width="16" height="14" viewBox="0 0 16 14"><rect width="16" height="14" rx="2" fill="#f47a20"/><path d="M4 4h8M4 7h8M4 10h5" stroke="#1b1b1b" stroke-width="1.4"/></svg>01632 960418</div>
    <div class="foot-line"><svg width="16" height="12" viewBox="0 0 16 12"><rect width="16" height="12" rx="1" fill="#f47a20"/><path d="M1 1l7 6 7-6" fill="none" stroke="#1b1b1b" stroke-width="1.4"/></svg>info@kolvexdigital-example.com</div>
  </div>
</footer>

</body>
</html>
```